Luxury Brand Real Estate For Sale sign

**Update** I've added some examples from the internet of other signs that have a look similar to what I would like to see. I do not want my personal name in the sign. And the word FOR SALE Does not need to be so large - it can be more subtle.
I want to create a Real Estate for sale sign for my company that will be used for luxury/higher end real estate listings. I’m sharing my business card as well as a logo with new teal color to show what we're moving towards: we’re using Teal, white, black and gold.
Hoping the sign is simple, sophisticated and eye catching.
The sign should be 24" wide by 30" tall including the company name: Harbor Crest Realty Group and our logo, office phone number 727-555-0148 and website www.hcrgexample.com the words "For Sale"
Optional to add this e-mail address info@hcrgexample.com to the sign
Target Market(s)
Luxury home buyers
Industry/Entity Type
Real Estate
Look and feel

```html
<!DOCTYPE html>
<html lang="en">
<head>
<meta charset="utf-8">
<title>Harbor Crest Realty Group – For Sale Sign</title>
<link rel="stylesheet" href="https://fonts.googleapis.com/css2?family=Josefin+Sans:wght@400;600;700&display=swap">
<style>
  :root {
    --backdrop: #b3b3b3;
    --sign-black: #1e1c1a;
    --sign-white: #ffffff;
    --ink: #1a1a1a;
    --gold-dark: #a9782f;
    --gold-mid: #d7b65a;
    --gold-light: #efe29a;
    --gold-gradient: linear-gradient(90deg, var(--gold-dark) 0%, var(--gold-mid) 30%, var(--gold-light) 55%, var(--gold-mid) 78%, var(--gold-dark) 100%);
  }
  * { margin: 0; padding: 0; box-sizing: border-box; }
  html, body {
    width: 1200px;
    height: 2404px;
    overflow: hidden;
    background: var(--backdrop);
  }
  .sign {
    position: absolute;
    left: 80px;
    top: 552px;
    width: 1040px;
    height: 1300px;
    background: var(--sign-white);
    font-family: "Josefin Sans", sans-serif;
    overflow: hidden;
  }
  .sign__panel {
    position: absolute;
    left: 0; top: 0;
    width: 100%;
    height: 974px;
    background: var(--sign-black);
  }
  .headline {
    position: absolute;
    left: 72px;
    font-weight: 700;
    font-size: 300px;
    line-height: 1;
    letter-spacing: -4px;
  }
  .headline--for { top: 76px; color: var(--sign-white); }
  .headline--sale {
    top: 348px;
    background: var(--gold-gradient);
    -webkit-background-clip: text;
    background-clip: text;
    color: transparent;
  }
  .gold-rule {
    position: absolute;
    left: 78px;
    top: 638px;
    width: 560px;
    height: 10px;
    border-radius: 5px;
    background: var(--gold-gradient);
  }
  .website {
    position: absolute;
    left: 66px;
    top: 690px;
    color: var(--sign-white);
    font-size: 60px;
    font-weight: 400;
    letter-spacing: 1px;
  }
  .website b { font-weight: 700; }
  .phone-pill {
    position: absolute;
    left: 70px;
    top: 898px;
    width: 900px;
    height: 152px;
    border-radius: 76px;
    background: var(--gold-gradient);
    box-shadow: 0 14px 16px -8px rgba(0,0,0,0.35);
    display: flex;
    align-items: center;
    justify-content: center;
  }
  .phone-pill__number {
    color: var(--ink);
    font-size: 132px;
    font-weight: 700;
    letter-spacing: -2px;
    padding-top: 18px;
  }
  .brand {
    position: absolute;
    left: 56px;
    top: 1086px;
    height: 156px;
    display: flex;
    align-items: center;
  }
  .brand__mark {
    width: 130px;
    height: 130px;
    border: 9px solid var(--ink);
  }
  .brand__divider {
    width: 5px;
    height: 156px;
    background: var(--ink);
    margin: 0 32px 0 40px;
  }
  .brand__name {
    color: var(--ink);
    font-weight: 600;
    line-height: 1;
  }
  .brand__name-top {
    display: block;
    font-size: 62px;
    letter-spacing: -1px;
  }
  .brand__name-bottom {
    display: block;
    font-size: 36px;
    letter-spacing: 14px;
    margin-top: 6px;
  }
</style>
</head>
<body>
  <main class="sign">
    <div class="sign__panel"></div>
    <h1 class="headline headline--for">FOR</h1>
    <div class="headline headline--sale">SALE</div>
    <div class="gold-rule"></div>
    <p class="website">www.<b>hcrgexample</b>.com</p>
    <div class="phone-pill"><span class="phone-pill__number">727-555-0148</span></div>
    <div class="brand">
      <div class="brand__mark"></div>
      <div class="brand__divider"></div>
      <p class="brand__name">
        <span class="brand__name-top">HARBOR CREST</span>
        <span class="brand__name-bottom">REALTY GROUP</span>
      </p>
    </div>
  </main>
</body>
</html>
```